900mm double sided Card Ponytail Insert for hair

I need print ready file designs for card packaging inserts for my line of ponytails, These are two sided colour and fold at each end or contain the hair, for structure and so the brand is on display. These will be marketed as luxury ponytails, so we want a simple, soft but luxurious design feel. All the details are below but it will be the logo, photos and simple messaging

Target Market(s)

18-30 females

Industry/Entity Type

Beauty

Font styles to use
Serif

Requirements
Must have
• - Lumera Logo on the back and top front fold.
'Luxury Synthetic Ponytails' Head line
'For effortlessly long and luxurious hair' tag line
'For tutorials, questions and inspiration head to our 'Brightroom' on lumerabeauty.com'
www.lumerabeauty.com
Tag us on socials! @lumerabeautyofficial (pictavo and Chatterloop logos)
3 step-by-step pictures (holding pictures please until i have some taken)
Nice to have
• (notes to designers) view our website to see our branding lumerabeauty.com - it would be good to use our brand colours and somekind of tropical leaves maybe? i'm thinking palm leaves?
- my brand font is Sweet Getaway - but this may only be good for the biggest headings

```html
<!DOCTYPE html>
<html lang="en">
<head>
<meta charset="utf-8">
<title>Lumera Ponytail Insert – Dieline</title>
<link rel="stylesheet" href="https://fonts.googleapis.com/css2?family=Open+Sans:wght@400;600&display=swap">
<style>
  :root {
    --backdrop: #979797;
    --card: #ffffff;
    --cut-line: #4a4a4a;
    --gold: #d8a55c;
    --forest: #0f5a4a;
    --spine: #1e1e1e;
  }
  * { margin: 0; padding: 0; box-sizing: border-box; }
  html, body { width: 862px; height: 1200px; overflow: hidden; background: var(--backdrop); }
  .sheet { position: relative; width: 862px; height: 1200px; background: var(--backdrop); font-family: "Open Sans", sans-serif; }
  .piece { position: absolute; background: var(--card); }
  .outlined { border: 1px solid var(--cut-line); }

  .tuck-tab { left: 264px; top: 70px; width: 186px; height: 44px; border-radius: 40px 40px 0 0; border: 1px solid var(--cut-line); border-bottom: none; }
  .lid { left: 264px; top: 111px; width: 186px; height: 187px; border-left: 1px solid var(--cut-line); }
  .dust-flap-left { left: 76px; top: 210px; width: 186px; height: 88px; border-radius: 30px 30px 0 0; }
  .dust-flap-right { left: 452px; top: 210px; width: 186px; height: 88px; border-radius: 30px 30px 0 0; }
  .glue-tab { left: 28px; top: 302px; width: 50px; height: 518px; border-radius: 14px 0 0 14px; }
  .back-panel { left: 76px; top: 298px; width: 189px; height: 515px; border: 1px solid var(--cut-line); }
  .front-panel { left: 264px; top: 298px; width: 188px; height: 515px; }
  .inner-panel { left: 452px; top: 298px; width: 186px; height: 515px; }
  .hang-tab { left: 666px; top: 258px; width: 131px; height: 42px; border-radius: 16px 16px 0 0; }
  .hang-hole { position: absolute; left: 723px; top: 269px; width: 20px; height: 20px; border-radius: 50%; background: var(--backdrop); }
  .info-panel { left: 638px; top: 298px; width: 189px; height: 523px; border: 1px solid var(--cut-line); }
  .base-flap-left { left: 76px; top: 813px; width: 186px; height: 179px; border-radius: 0 0 30px 30px; }
  .base-tuck { left: 264px; top: 813px; width: 186px; height: 185px; border-radius: 0 0 34px 34px; border: 1px solid var(--cut-line); border-top: none; }
  .base-flap-right { left: 452px; top: 813px; width: 186px; height: 83px; border-radius: 0 0 30px 30px; }

  .wordmark { position: absolute; color: var(--gold); font-weight: 400; letter-spacing: 1px; text-align: center; }
  .wordmark--lid { left: 264px; top: 192px; width: 186px; font-size: 30px; }
  .wordmark--front { left: 264px; top: 370px; width: 186px; font-size: 42px; }

  .headline { position: absolute; left: 264px; top: 472px; width: 188px; height: 52px; border-top: 3px solid var(--forest); border-bottom: 3px solid var(--forest); color: var(--forest); font-size: 16.5px; line-height: 20px; letter-spacing: 1.6px; padding: 4px 0 0 4px; }
  .tagline { position: absolute; left: 265px; top: 538px; color: var(--gold); font-size: 15px; line-height: 20px; }

  .info-copy { position: absolute; left: 638px; top: 298px; width: 189px; height: 523px; }
  .info-copy__rotated { position: absolute; left: 50%; top: 50%; width: 300px; transform: translate(-50%, -50%) rotate(-90deg); text-align: center; color: var(--gold); }
  .info-copy__note { font-size: 10.5px; line-height: 14px; }
  .info-copy__url { font-size: 21px; line-height: 28px; margin-top: 10px; }

  .window { position: absolute; left: 0; top: 0; }
</style>
</head>
<body>
<main class="sheet">
  <div class="piece tuck-tab"></div>
  <div class="piece lid"></div>
  <div class="piece dust-flap-left"></div>
  <div class="piece dust-flap-right"></div>
  <div class="piece glue-tab"></div>
  <div class="piece back-panel"></div>
  <div class="piece front-panel"></div>
  <div class="piece inner-panel"></div>
  <div class="piece hang-tab"></div>
  <div class="hang-hole"></div>
  <div class="piece info-panel"></div>
  <div class="piece base-flap-left"></div>
  <div class="piece base-tuck"></div>
  <div class="piece base-flap-right"></div>

  <div class="wordmark wordmark--lid">Lumera</div>
  <div class="wordmark wordmark--front">Lumera</div>

  <h1 class="headline">Luxury Synthetic<br>Ponytails</h1>
  <p class="tagline">For effortlessly<br>Long &amp;<br>Luxurious<br>Hair</p>

  <svg class="window" width="862" height="1200" viewBox="0 0 862 1200" aria-hidden="true">
    <path fill="var(--backdrop)" d="M452,428 C452,520 380,580 330,640 C290,690 276,730 284,760 C288,778 296,790 304,798 L598,798 C606,790 614,778 618,760 C626,730 612,690 572,640 C522,580 452,520 452,428 Z"/>
    <line x1="452" y1="432" x2="452" y2="798" stroke="var(--spine)" stroke-width="2.5"/>
  </svg>

  <div class="info-copy">
    <div class="info-copy__rotated">
      <p class="info-copy__note">'For tutorials, questions and inspiration<br>head to our 'Brightroom'</p>
      <p class="info-copy__url">www.lumerabeauty.com</p>
    </div>
  </div>
</main>
</body>
</html>
```